Stride & Mend Email Marketing

We need an email newsletter design/template that can help us advertise our services and explain what our company is all about. Although we have a lot of text, we'd like something inviting and simple, perhaps with a powerful banner/images and really clear, precise graphics and touches that make the email look inviting and stand out.

Because this will be blasted to many people, we'd like them to take a second look. So the design and layout must really be top notch prior to the reader actually taking time to read the content.

Stride & Mend is basically a health consultancy that helps patients all over Africa, organize and facilitate their health care in South Africa. So say a person was sick in Kenya. That person might want to go to South Africa, best known for treatment and health care in the continent, however, they might not know where to start looking for doctors, hospitals, or even accommodation and logistics. That is where Stride & Mend comes in. They take care of all of those things for you, by allowing you to consult with a Doctor who can advise you and arrange all of those logistical nightmares.

******Also the Newsletter we want to put up is uploaded in the Microsoft Word document. Please use the content in the document.******

******And we may look to get someone to code the design as an HTML, so we're looking for really good designs.********

Target Market(s)

The target market is well to do people who would spend money to travel to South Africa for medical treatment. So these people are well travelled, college educated, well to do.

Industry/Entity Type

Accommodation

Font styles to use
Serif

Requirements
Must have
• Include the logo in the header,
Include an area for social media contact details/icons in the footer
Nice to have
• A clean, nice image or graphic health related that makes up the header

```html
<!DOCTYPE html>
<html lang="en">
<head>
<meta charset="utf-8">
<title>Stride &amp; Mend Newsletter</title>
<link href="https://fonts.googleapis.com/css2?family=Arimo:wght@400;700&display=swap" rel="stylesheet">
<style>
:root{
  --page-bg:#f0f0f0;
  --top-band:#e4e4e4;
  --bottom-band:#e2e2e2;
  --sheet:#ffffff;
  --green:#6ea354;
  --green-bright:#5cb833;
  --text:#6b6b6b;
  --text-strong:#444444;
  --rule:#e6e6e6;
  --social-strip:#ececec;
  --social-dot:#dcdcdc;
  --footer:#393a48;
  --footer-text:#ffffff;
  --footer-muted:#b9bac4;
  --square-a:#3b5998;
  --square-b:#2aa3de;
  --square-c:#1f6fa8;
}
*{margin:0;padding:0;box-sizing:border-box}
html,body{width:1200px;height:2263px;overflow:hidden}
body{
  position:relative;
  background:var(--page-bg);
  font-family:"Arimo",Arial,sans-serif;
  color:var(--text);
}
.band-top{position:absolute;left:0;top:0;width:1200px;height:121px;background:var(--top-band)}
.band-bottom{position:absolute;left:0;top:1814px;width:1200px;height:449px;background:var(--bottom-band)}
.sheet{position:absolute;left:240px;top:0;width:720px;height:1814px;background:var(--sheet)}
.inner{position:absolute;left:36px;width:648px}

.brand{position:absolute;left:36px;top:36px;display:flex;align-items:center;gap:12px}
.brand-dot{width:30px;height:30px;border-radius:50%;background:var(--green-bright)}
.brand-name{font-size:38px;font-weight:700;color:var(--green-bright);letter-spacing:.5px}
.header-right{position:absolute;right:44px;top:26px;text-align:right}
.header-squares{display:flex;justify-content:flex-end;gap:14px;margin-bottom:10px}
.header-squares span{width:30px;height:30px;border-radius:4px;display:block}
.header-squares span:nth-child(1){background:var(--square-a)}
.header-squares span:nth-child(2){background:var(--square-b)}
.header-squares span:nth-child(3){background:var(--square-c)}
.call{font-size:19px;color:#888;letter-spacing:-.5px}
.call b{color:var(--green-bright)}

.hero{top:155px;height:301px;background:linear-gradient(100deg,#e7e5df 0%,#9fd2cd 30%,#dfd8cf 55%,#8a6a57 78%,#7ea7c8 100%)}
.headline{top:470px;font-size:22px;line-height:29px;font-weight:700;color:var(--green)}
.copy{font-size:16.5px;line-height:24.5px}
.copy b{color:var(--text-strong)}
.intro{top:548px}
.intro p+p{margin-top:24px}

.columns{top:785px;display:flex;gap:36px}
.col{width:306px}
.col-photo{height:143px}
.col-photo.doctor{background:linear-gradient(90deg,#f6f6f6 0%,#efe9e4 45%,#7b5443 60%,#f4f4f4 80%)}
.col-photo.patient{background:linear-gradient(100deg,#7ea9c9 0%,#5d3d31 35%,#8cb3cf 55%,#e6ddd2 80%,#9fd2cd 100%)}
.col h2{font-size:22px;font-weight:700;color:var(--green);margin:22px 0 12px}

.contact{top:1198px;text-align:center;font-size:16.5px;line-height:24px}
.contact .lines{margin-top:24px}
.green{color:var(--green-bright);font-weight:700}
.link{color:var(--green-bright);font-weight:700;border-bottom:1px solid var(--green-bright)}
.rule{top:1372px;height:1px;background:var(--rule)}

.services-title{top:1400px;font-size:22px;line-height:29px;font-weight:700;color:var(--green)}
.services{top:1476px;list-style:none;font-size:16.5px;line-height:23px}
.services li{padding-left:10px;text-indent:-10px;margin-bottom:10px}
.services li::before{content:"• "}

.social{position:absolute;left:240px;top:1814px;width:720px;height:91px;background:var(--social-strip);display:flex;align-items:center;padding:0 36px}
.social h3{font-size:22px;font-weight:400;color:var(--text-strong);letter-spacing:-.3px;margin-right:auto}
.social-dots{display:flex;gap:12px}
.social-dots span{width:41px;height:41px;border-radius:50%;background:var(--social-dot);display:block}

.footer{position:absolute;left:240px;top:1905px;width:720px;height:235px;background:var(--footer);color:var(--footer-text);padding:0 36px}
.footer-info{text-align:center;font-size:16.5px;line-height:29px;padding-top:19px}
.footer-info .lines{margin-top:22px;line-height:24px}
.footer .link,.footer .green{color:#8fce6a;border-color:#8fce6a}
.footer .site{color:#fff;border-bottom:1px solid #fff}
.footer-rule{height:1px;background:#5a5b68;margin-top:12px}
.footer-base{display:flex;justify-content:space-between;font-size:14px;color:var(--footer-muted);padding-top:20px}
.footer-base b{color:#fff;font-weight:400}
</style>
</head>
<body>
<div class="band-top"></div>
<div class="band-bottom"></div>

<main class="sheet">
  <div class="brand"><span class="brand-dot"></span><span class="brand-name">Stride &amp; Mend</span></div>
  <div class="header-right">
    <div class="header-squares"><span></span><span></span><span></span></div>
    <div class="call">Call us today: <b>+1800.555.0199</b></div>
  </div>

  <div class="inner hero" role="img" aria-label="Photo of a smiling doctor with a stethoscope consulting a patient"></div>

  <h1 class="inner headline">Health is a Priority and Not an Option! Don't take chances when options are very close to home!</h1>

  <div class="inner copy intro">
    <p><b>Stride &amp; Mend (S&amp;M)</b> is your link to excellent health care in South Africa. Whether you are suffering from general ill health, require emergency medical attention or need preventative health care, Stride and Mend can HELP you. It was founded and is managed by Dr. Amani Okello, a Tanzanian doctor who knows all too well that misdiagnosis in the African continent is common and health issues are very often mistreated due to a lack of specialized medical knowledge and poor medical facilities.</p>
    <p>This leads to premature death and chronic disability.</p>
  </div>

  <div class="inner columns">
    <section class="col">
      <div class="col-photo doctor" role="img" aria-label="Photo of a doctor in a white coat with a stethoscope"></div>
      <h2>Dr. Amani is a phone call away</h2>
      <p class="copy">A doctor trained to manage your chronic/longstanding illness or emergency situation – by providing advice, ensuring that your health condition is accurately diagnosed, and linking you to the <b>best solution possible as close to home</b> as possible.</p>
    </section>
    <section class="col">
      <div class="col-photo patient" role="img" aria-label="Photo of a patient holding his shoulder during a consultation"></div>
      <h2>Best Health Care System</h2>
      <p class="copy">There is no doubt that South Africa offers the <b>best health care system within the African Continent</b> and Dr. Amani and her team, will manage a medical evacuation from your home country and provide support throughout the treatment process in South Africa.</p>
    </section>
  </div>

  <div class="inner contact copy">
    <p>By contacting Stride and Mend, &nbsp;you will have the comfort that you and your family can experience a <b>seamless and hassle-free</b> patient journey process.</p>
    <p class="lines">Phone: <span class="green">+1800.555.0199</span><br>Email: <span class="link">hello@stridemend.com</span></p>
  </div>

  <div class="inner rule"></div>

  <h2 class="inner services-title">Stride&amp; Mend will facilitate the following services for your patient journey process:</h2>
  <ul class="inner services">
    <li>Initial contact with a health care professional to ensure you are guided to an appropriate specialist who can manage your health problem</li>
    <li>Provide access to the most reputable hospitals and healthcare providers in SA</li>
    <li>Schedule appointments with specialists</li>
    <li>Manage all travel arrangements</li>
    <li>Organise hotel or chosen accommodation option</li>
    <li>Transport to and from the airport</li>
    <li>Transport to and from hospital (for all your medical requirements)</li>
    <li>Access to medical evacuation services from home country – Air Ambulance Service</li>
  </ul>
</main>

<section class="social">
  <h3>STAY CONNECTED</h3>
  <div class="social-dots"><span></span><span></span><span></span><span></span><span></span><span></span><span></span><span></span></div>
</section>

<footer class="footer">
  <div class="footer-info">
    <p>For further information, visit our website: &nbsp;<span class="site">www.strideandmend.co.za</span> or contact us with information provided below.</p>
    <p class="lines">Phone: <span class="green">+1800.555.0199</span><br>Email: <span class="link">hello@stridemend.com</span></p>
  </div>
  <div class="footer-rule"></div>
  <div class="footer-base">
    <span>Copyright 2014 <b>Stride and Mend</b>. All Rights Reserved.</span>
    <span>View Online &nbsp;| &nbsp;Unsubscribe</span>
  </div>
</footer>
</body>
</html>
```